Update Existing Homepage

Here’s the scoop… we want to update our homepage here with a more modern look: wws.Pagelore-Hub.com

I am NOT looking for a brand new design; as our site has many pages, and section. Instead I want a new more modern design based on the existing design (if that make sense)

Whatever new design…must match the rest of the site
I want the current header (menu and up) as well as the current footer to stay the same; it’s everything in between that has to change.

What I’m really looking for is:

- Better use of space
- Better emphasis on key components
- Addition of a new section (more about that below)
- More modern feel

By modern I mean the icons we use are getting a bit cheesy, the straight layout is also dated, etc

Here are the elements that I need to have on the page in ORDER OF IMPORTANCE:

1) ADVERTISING SPACE: while I don’t want huge flashing ads front and center, this being an information site, ads are our #1 source of revenue and as such are important. I would like to see several add slots of various sizes (standard sizes) throughout the page in eye catching spots (not hidden in the bottom right corner)

2) ARTICLES: articles are our main draw. If you look at the current design you will see there is a lead article at the top left of the page and then a series of other articles down the middle

3) NEWSLETTER SUBSCRIPTION BOX: need to have a section that is highly visible for people to subscribe to our newsletter (doesn’t have to be as big as the existing one)

4) BLOG POSTS (‘the experts say’ section): besides articles we also have blog posts. However I’m thinking we could combine the articles and the blog posts into 1 section titled “news” or something to save space. And the blog posts could just have an identifier at the beginning of the title such as “Blog: post title”

5) VIDEOS: don’t need to show a ton of vids, but would like room for 1 main video and a few suggestions of others.

What I have seen a bunch of new websites use is a type rotating ‘newsboard’, like the one on the zinkora homepage for example. Perhaps using an idea like that could be cool. You could feature 1 article, 1 blog post, 1 video, or something in it and have it rotate.

6) RESOURCES: This is something that is not ‘really’ currently on the homepage. By that I mean there is a “webmaster resources” section + a “webmaster tools” section but these are dated. Dated because we recently added a new directory to the site: http://resources.pagelore-hub.com/ - so what I would like to do now is combine those 2 section; 1) invite people to check out the directory + submit there and 2) list a few of the newer entries (ie. new entries automatically get posted on the section of our homepage

7) FORUM DISCUSSIONS: if you look at the “Industry Discussions and Help” section, those are the latest discussions from our forums http://forums.pagelore-hub.com/

That is it…good luck,

Tam

Target Market(s)

web professionals

Industry/Entity Type

Industry

Requirements
Must have
• see description
Nice to have
• see description
Should not have
• see description

```html
<!DOCTYPE html>
<html lang="en">
<head>
<meta charset="utf-8">
<title>Pagelore Hub – Helping You Succeed Online</title>
<link rel="stylesheet" href="https://fonts.googleapis.com/css2?family=Arimo:wght@400;700&display=swap">
<style>
:root{
  --lime:#c4dc2e;
  --lime-dark:#a6c016;
  --lime-light:#e3f08a;
  --pink:#c24aa3;
  --pink-dark:#a3338a;
  --pink-light:#d76fbf;
  --link:#3b9fe0;
  --link-dark:#1f7fc4;
  --label-green:#7aa514;
  --title-green:#8dba19;
  --text:#555;
  --muted:#888;
  --line:#e1e1e1;
  --ad-fill:#e4e4e4;
  --ad-text:#b4b4b4;
  --page:#f4f4f4;
  --white:#fff;
  --ad-link:#1a2fc9;
  --ad-url:#2a8a2a;
}
*{box-sizing:border-box;margin:0;padding:0}
html,body{width:1200px;height:2169px;overflow:hidden}
body{font-family:"Arimo",Arial,sans-serif;color:var(--text);background:var(--white)}
.page{position:relative;width:1200px;height:2169px;overflow:hidden;
  background:linear-gradient(#f2f2f2,#fff 160px,#fff 2000px,#f0f0f0)}
.abs{position:absolute}
a{color:var(--link);text-decoration:none}

/* ad slots */
.ad{position:absolute;background:var(--white);border:1px solid var(--line);border-radius:6px;padding:4px 6px}
.ad-tag{font-size:10px;color:var(--muted);display:block;height:14px}
.ad-tag::before{content:"› ";color:var(--pink)}
.ad-area{background:linear-gradient(#ececec,#dcdcdc);color:var(--ad-text);font-size:25px;line-height:1.1;padding:6px 10px;position:absolute}

/* header */
.header{left:69px;top:169px;width:1055px;height:104px;background:var(--white);border:1px solid var(--line);border-bottom:none}
.header-deco{left:380px;top:0;width:300px;height:104px;background:radial-gradient(ellipse at center,#efefef,rgba(255,255,255,0) 70%)}
.header-deco-r{left:830px;top:0;width:225px;height:104px;background:radial-gradient(ellipse at center,#f0f0f0,rgba(255,255,255,0) 70%)}
.brand{left:92px;top:28px;display:flex;align-items:center;gap:10px}
.brand-dot{width:26px;height:26px;border-radius:50%;background:var(--pink)}
.brand-name{font-size:28px;font-weight:700;color:#333;letter-spacing:-.3px}
.brand-tag{left:128px;top:66px;font-size:14px;font-weight:700;color:var(--label-green);letter-spacing:.5px}
.search{left:581px;top:10px;width:474px;height:44px;background:#f1f1f1;border-radius:4px}
.search-field{left:28px;top:11px;width:306px;height:18px;background:var(--white);border:1px solid #ccc}
.search-btn{left:358px;top:2px;width:100px;height:38px;background:linear-gradient(var(--lime-light),var(--lime));border:1px solid var(--lime-dark);font-size:12px;color:#333;display:flex;align-items:center;justify-content:center}
.lang{left:972px;top:73px;font-size:14px;color:#555;display:flex;align-items:center;gap:6px}
.lang i{width:14px;height:14px;border-radius:50%;background:#3b82d0;display:block}

.nav{left:0;top:273px;width:1200px;height:54px;background:linear-gradient(#fff,#ececec);border-top:1px solid #ddd;border-bottom:1px solid #ccc}
.nav ul{list-style:none;position:absolute;left:76px;top:0;display:flex;height:54px}
.nav li{height:54px;display:flex;align-items:center;justify-content:center;font-size:14px;font-weight:700;color:#222;border-right:1px solid #d2d2d2}
.nav li:first-child{border-left:1px solid #d2d2d2}
.nav li.active{background:var(--lime);color:#333}
.nav-band{left:76px;top:327px;width:1048px;height:28px;background:linear-gradient(var(--lime),var(--lime-light))}

/* panels */
.panel{position:absolute;background:var(--white);border:1px solid var(--line);border-radius:4px}
.lead{left:76px;top:380px;width:690px;height:305px;overflow:hidden}
.lead-tick{left:28px;top:24px}
.kicker{font-size:12px;color:var(--label-green);font-weight:700;letter-spacing:.3px}
.lead-kicker{left:98px;top:17px}
.lead-title{left:98px;top:37px;width:400px;font-size:22px;line-height:1.45;color:var(--title-green);font-weight:400}
.lead-meta{left:20px;top:126px;font-size:11px;color:var(--muted);line-height:1.8;font-weight:700}
.lead-excerpt{left:20px;top:178px;width:475px;font-size:12px;line-height:1.75;color:#666}
.more{font-size:11px;font-weight:700;color:var(--link-dark)}
.more::before{content:"➜ ";color:var(--link)}
.lead-more{left:20px;top:272px}
.lead-all{left:380px;top:272px}
.tabs{left:510px;top:0;width:180px;height:305px}
.tab{position:absolute;left:0;width:180px;height:101px;background:linear-gradient(var(--pink-light),var(--pink));color:var(--white);font-size:25px;line-height:1.1}
.tab span{position:absolute;left:70px}
.tab-icon{position:absolute;left:20px;width:34px;height:38px}
.tab-notch{position:absolute;left:-12px;top:40px;width:0;height:0;border-top:12px solid transparent;border-bottom:12px solid transparent;border-right:12px solid var(--pink-light)}

/* text ads */
.text-ads{left:783px;top:702px;width:330px;height:284px;background:var(--white)}
.text-ad{position:absolute;left:2px;width:320px;font-size:13px;line-height:1.35;color:#222}
.text-ad b{color:var(--ad-link);text-decoration:underline;font-size:14px;display:block}
.text-ad small{color:var(--ad-url);font-size:9px;display:block}
.text-ads-nav{left:2px;top:264px;display:flex;gap:3px}
.text-ads-nav i{width:15px;height:15px;display:block;background:#ccc}
.text-ads-nav i.on{background:#1a2fc9}
.text-ads-bar{left:225px;top:247px;width:86px;height:14px;border:1px solid #bbb}

/* section bars */
.bar{position:absolute;height:55px;background:linear-gradient(var(--lime-light),var(--lime));border-radius:4px;color:#333;font-size:30px;display:flex;align-items:center}
.news-bar{left:76px;top:713px;width:688px;padding-left:76px}
.news-icon{left:10px;top:8px}
.rss{left:644px;top:15px;width:28px;height:28px;border-radius:5px;background:linear-gradient(#f7a23a,#e26e12)}
.news-tabs{left:86px;top:782px;display:flex;gap:4px}
.news-tab{height:34px;padding:0 20px;display:flex;align-items:center;background:linear-gradient(#f4f4f4,#d9d9d9);border:1px solid #c9c9c9;border-bottom:none;border-radius:4px 4px 0 0;font-size:17px;color:#666}
.news-tab.on{background:linear-gradient(#f0b3e0,#dd88ca);color:var(--white);border-color:#d07bbf}
.news-rule{left:76px;top:816px;width:688px;height:1px;background:#ccc}
.news-item{position:absolute;left:76px;width:688px;border-bottom:1px solid var(--line)}
.avatar{position:absolute;left:0;width:46px;height:46px;border-radius:50%;background:linear-gradient(#f1c9a3,#c78a52)}
.doc-icon{position:absolute;left:2px;width:40px;height:42px}
.news-kicker{position:absolute;left:57px;font-size:12px;color:var(--label-green)}
.news-kicker em{font-style:normal;color:var(--pink)}
.news-title{position:absolute;left:57px;width:600px;font-size:19px;line-height:1.38;color:var(--link)}
.cat-list{left:76px;top:1177px;list-style:none;font-size:12px;font-weight:700;line-height:20px;color:var(--link-dark)}
.cat-list li::before{content:"➜ ";color:var(--link)}

/* resources & forums */
.res-bar{left:76px;top:1426px;width:333px;padding-left:14px}
.forum-bar{left:429px;top:1426px;width:334px;padding-left:14px}
.sponsor{position:absolute;right:10px;top:4px;width:96px;height:46px;background:#eee;border-radius:3px;font-size:9px;color:#555;text-align:center}
.sponsor span{display:block;margin:13px auto 0;width:86px;height:26px;background:#d3d3d3;color:#999;font-size:17px;line-height:26px}
.sub-title{font-size:14px;font-weight:700;color:var(--pink-dark)}
.res-title{left:76px;top:1498px}
.forum-title{left:429px;top:1498px}
.res-copy{left:76px;top:1525px;width:330px;font-size:12px;line-height:1.7;color:#666}
.pink-btn{position:absolute;top:1620px;width:157px;height:132px;border-radius:6px;background:linear-gradient(var(--pink-light),var(--pink));box-shadow:0 3px 4px rgba(0,0,0,.2);color:rgba(255,255,255,.9);font-size:17px;font-weight:700;text-align:center;line-height:1.2}
.pink-btn span{position:absolute;left:0;right:0;top:78px}
.pink-btn svg{position:absolute;left:52px;top:18px}
.latest-res{left:76px;top:1770px;width:333px;height:44px;background:linear-gradient(#fff,#e5e5e5);font-size:25px;color:#333;padding:6px 0 0 2px}
.res-list{left:76px;top:1828px;list-style:none}
.res-list li{height:35px;display:flex;align-items:center;gap:12px;font-size:18px;color:var(--link)}
.gear{width:22px;height:22px;border-radius:50%;border:5px solid #aaa;background:#eee}
.res-all{left:76px;top:1945px}
.forum-list{left:429px;top:1526px;list-style:none;width:330px}
.forum-list li{position:relative;padding-left:40px;font-size:17px;font-weight:700;color:var(--link);line-height:1.15;margin-bottom:14px}
.forum-list svg{position:absolute;left:0;top:2px}
.forum-all{left:429px;top:1947px}

/* newsletter */
.nl-bar{left:783px;top:995px;width:345px;height:55px;font-size:22px;padding-left:14px;border-radius:4px 4px 0 0}
.nl-copy{left:786px;top:1061px;width:340px;font-size:12px;line-height:1.6;color:#666}
.nl-label{position:absolute;left:786px;font-size:12px;font-weight:700;color:var(--pink-dark)}
.nl-field{position:absolute;left:786px;width:342px;height:28px;border:1px solid #d4d4d4;background:linear-gradient(#f2f2f2,#fff)}
.nl-privacy{left:786px;top:1321px;width:342px;font-size:12px;line-height:1.7;color:#666}
.nl-privacy a{color:var(--link)}
.nl-btn{left:786px;top:1376px;width:118px;height:31px;border-radius:5px;background:linear-gradient(var(--pink-light),var(--pink));color:var(--white);font-size:12px;font-weight:700;display:flex;align-items:center;justify-content:center}

/* footer */
.footer{left:0;top:2036px;width:1200px;height:133px;background:linear-gradient(#e9e9e9,#f7f7f7 40%,#f2f2f2);border-top:1px solid #ddd}
.foot-links{left:0;top:58px;width:1200px;text-align:center;font-size:13px;color:#555;word-spacing:2px}
.foot-copy{left:0;top:101px;width:1200px;text-align:center;font-size:13px;color:#555}
.foot-copy b{color:#333}
</style>
</head>
<body>
<div class="page">

  <!-- top leaderboard -->
  <div class="ad" style="left:199px;top:9px;width:804px;height:131px">
    <span class="ad-tag">Add</span>
    <div class="ad-area" style="left:12px;top:28px;width:780px;height:94px">Leaderboard 728x90</div>
  </div>

  <!-- header -->
  <header class="abs header">
    <div class="abs header-deco" role="img" aria-label="Faint mascot decoration"></div>
    <div class="abs header-deco-r" role="img" aria-label="Faint mascot decoration"></div>
    <div class="abs brand"><span class="brand-dot"></span><span class="brand-name">Pagelore Hub</span></div>
    <div class="abs brand-tag">Helping You Succeed Online</div>
    <div class="abs search">
      <div class="abs search-field"></div>
      <div class="abs search-btn">Searchly Search</div>
    </div>
    <div class="abs lang"><i></i>English</div>
  </header>

  <nav class="abs nav">
    <ul>
      <li class="active" style="width:92px">Home</li>
      <li style="width:94px">Forums</li>
      <li style="width:108px">Videos</li>
      <li style="width:98px">Articles</li>
      <li style="width:138px">Publications</li>
      <li style="width:113px">SEO Blog</li>
      <li style="width:162px">Marketing Blog</li>
      <li style="width:118px">Resources</li>
      <li style="width:121px">Advertise</li>
    </ul>
  </nav>
  <div class="abs nav-band"></div>

  <!-- lead article -->
  <section class="panel lead">
    <svg class="abs lead-tick" width="52" height="48" viewBox="0 0 52 48"><path d="M3 26 L18 42 L49 4" fill="none" stroke="#49a51b" stroke-width="8" stroke-linecap="round" stroke-linejoin="round"/></svg>
    <div class="abs kicker lead-kicker">ARTICLES</div>
    <h1 class="abs lead-title">5 Reasons to Build Multiple Niche Websites and Leverage Them</h1>
    <div class="abs lead-meta">Published on May 14, 2010<br>by Marla Quinlan</div>
    <p class="abs lead-excerpt">Multiple niche websites are a great way to cover all aspects of a business and expand your market reach. Having multiple websites which cover a lot of ground for one business is the latest trend in the field of search engine optimization.</p>
    <a class="abs more lead-more">Read more</a>
    <a class="abs more lead-all">See all articles</a>
    <div class="abs tabs">
      <div class="tab" style="top:0"><span class="tab-notch"></span>
        <svg class="tab-icon" style="top:30px" viewBox="0 0 34 38"><rect x="2" y="2" width="26" height="34" fill="#fff"/><path d="M7 12h16M7 18h16M7 24h12" stroke="#bbb" stroke-width="2"/><path d="M31 6 L18 30" stroke="#e8a21a" stroke-width="4"/></svg>
        <span style="top:33px">Articles</span></div>
      <div class="tab" style="top:102px;border-top:1px solid #e9a6d8">
        <svg class="tab-icon" style="top:32px" viewBox="0 0 34 38"><rect x="2" y="10" width="30" height="24" fill="#222"/><path d="M2 4 L32 0 L32 8 L2 10Z" fill="#444"/></svg>
        <span style="top:35px">Videos</span></div>
      <div class="tab" style="top:204px;border-top:1px solid #e9a6d8">
        <svg class="tab-icon" style="top:30px" viewBox="0 0 34 38"><rect x="2" y="2" width="28" height="34" fill="#eee"/><path d="M7 10h18M7 16h18M7 22h18M7 28h12" stroke="#aaa" stroke-width="2"/></svg>
        <span style="top:22px">Blog<br>post</span></div>
    </div>
  </section>

  <!-- medium rectangle -->
  <div class="ad" style="left:783px;top:380px;width:345px;height:305px">
    <span class="ad-tag">Add</span>
    <div class="ad-area" style="left:12px;top:24px;width:320px;height:270px">Medium Rectangle<br>300x250</div>
  </div>

  <!-- text ads -->
  <aside class="abs text-ads">
    <div class="text-ad" style="top:0"><b>Online Email Marketing</b>Expand Your Business Quickly w/ Our User-Friendly Software! Free Trial.<small>www.mailvantor.com</small></div>
    <div class="text-ad" style="top:84px"><b>Web site not available ?</b>We monitor your web site non-stop. Instant email &amp; sms alert. Reports.<small>www.uptrellis.com</small></div>
    <div class="text-ad" style="top:168px"><b>Study Digital Marketing</b>Brennard Business School Next Round Ends Jun 27th—Apply Now!<small>www.brennard.edu/masters-program/</small></div>
    <div class="abs text-ads-bar"></div>
    <div class="abs text-ads-nav"><i></i><i class="on"></i><i></i></div>
  </aside>

  <!-- news -->
  <div class="bar news-bar">News
    <svg class="abs news-icon" width="52" height="42" viewBox="0 0 52 42"><rect x="10" y="4" width="32" height="34" fill="#fff" stroke="#bbb"/><path d="M4 10 L18 2 L22 30 L8 38Z" fill="#3a7fd0"/><path d="M16 14h20M16 20h20M16 26h16" stroke="#ccc" stroke-width="2"/></svg>
    <div class="abs rss"><svg width="28" height="28" viewBox="0 0 28 28"><circle cx="8" cy="20" r="3" fill="#fff"/><path d="M6 12a10 10 0 0 1 10 10M6 6a16 16 0 0 1 16 16" fill="none" stroke="#fff" stroke-width="3"/></svg></div>
  </div>
  <div class="abs news-tabs">
    <div class="news-tab on">LASTEST</div>
    <div class="news-tab">ARTICLES</div>
    <div class="news-tab">SEO BLOG</div>
    <div class="news-tab">MARKETING BLOG</div>
  </div>
  <div class="abs news-rule"></div>

  <article class="news-item" style="top:832px;height:72px">
    <div class="avatar" style="top:4px" role="img" aria-label="Author portrait"></div>
    <div class="news-kicker" style="top:6px">BLOG POST &nbsp;·&nbsp; <em>SEO BLOG THE EXPERTS SAY...</em></div>
    <div class="news-title" style="top:24px">Searchly Uses Semantic Closeness as a Ranking Factor</div>
  </article>
  <article class="news-item" style="top:914px;height:72px">
    <svg class="doc-icon" style="top:4px" viewBox="0 0 40 42"><rect x="2" y="2" width="34" height="38" rx="3" fill="#fff" stroke="#999" stroke-width="2"/><path d="M8 12h22M8 18h22M8 24h16" stroke="#bbb" stroke-width="2"/><path d="M36 6 L20 34" stroke="#e8a21a" stroke-width="4"/></svg>
    <div class="news-kicker" style="top:8px">ARTICLES</div>
    <div class="news-title" style="top:28px">Do Not Make These 10 Common SEO Mistakes</div>
  </article>
  <article class="news-item" style="top:992px;height:96px">
    <div class="avatar" style="top:4px" role="img" aria-label="Author portrait"></div>
    <div class="news-kicker" style="top:6px">BLOG POST &nbsp;·&nbsp; <em>MARKETING BLOG THE EXPERTS SAY...</em></div>
    <div class="news-title" style="top:24px">Study: Paymora Reveals Why Consumers Abandon Sites During Checkout</div>
  </article>
  <article class="news-item" style="top:1095px;height:72px">
    <svg class="doc-icon" style="top:4px" viewBox="0 0 40 42"><rect x="2" y="2" width="34" height="38" rx="3" fill="#fff" stroke="#999" stroke-width="2"/><path d="M8 12h22M8 18h22M8 24h16" stroke="#bbb" stroke-width="2"/><path d="M36 6 L20 34" stroke="#e8a21a" stroke-width="4"/></svg>
    <div class="news-kicker" style="top:8px">ARTICLES</div>
    <div class="news-title" style="top:28px">Online Reputation Management Advice</div>
  </article>

  <ul class="abs cat-list">
    <li>SEO Articles</li>
    <li>Internet Marketing Articles</li>
    <li>Development Articles</li>
    <li>General Articles</li>
    <li>And also in our Archives</li>
  </ul>

  <!-- full banner -->
  <div class="ad" style="left:156px;top:1310px;width:520px;height:94px">
    <span class="ad-tag">Add</span>
    <div class="ad-area" style="left:10px;top:22px;width:500px;height:64px">Full Banner<br>468x60</div>
  </div>

  <!-- newsletter -->
  <div class="bar nl-bar">Get The Latest Online Strategies</div>
  <p class="abs nl-copy">Get all the latest webmaster tips and tricks from some of the brightest minds in the online world delivered right to your inbox with the Pagelore-Hub Newsletter.</p>
  <label class="nl-label" style="top:1134px">Last name:</label>
  <div class="nl-field" style="top:1157px"></div>
  <label class="nl-label" style="top:1196px">First name:</label>
  <div class="nl-field" style="top:1220px"></div>
  <label class="nl-label" style="top:1261px">Your e-mail:</label>
  <div class="nl-field" style="top:1283px"></div>
  <p class="abs nl-privacy">Your <a>privacy</a> is 100% Guaranteed. Easily <a>unsubscribe</a> at any time.</p>
  <div class="abs nl-btn">SUBSCRIBE ME</div>

  <!-- resources -->
  <div class="bar res-bar">Resources<div class="sponsor">Sponsored by:<span>88x31</span></div></div>
  <h3 class="abs sub-title res-title">Get Listed in the PH Directory Now!</h3>
  <p class="abs res-copy">If you have a product or service aimed at web professionals, and want to expose yourself to 100,000+ monthly visitors add yourself to the Pagelore-Hub directory.</p>
  <div class="pink-btn" style="left:76px">
    <svg width="54" height="46" viewBox="0 0 54 46"><path d="M2 14h28V2l22 21-22 21V32H2Z" fill="#b6d633" stroke="#7a9a10" stroke-width="2"/></svg>
    <span>Submit your<br>bussiness</span></div>
  <div class="pink-btn" style="left:250px">
    <svg width="54" height="50" viewBox="0 0 54 50"><path d="M8 42 L42 8" stroke="#e8e8e8" stroke-width="7" stroke-linecap="round"/><path d="M10 8 L44 42" stroke="#bbb" stroke-width="7" stroke-linecap="round"/></svg>
    <span>More webmaster<br>Resources</span></div>
  <div class="abs latest-res">Lastest resources</div>
  <ul class="abs res-list">
    <li><i class="gear"></i>RSS Parser</li>
    <li><i class="gear"></i>Keyword Density</li>
    <li><i class="gear"></i>Verify Your Site</li>
  </ul>
  <a class="abs more res-all">See all resources</a>

  <!-- forums -->
  <div class="bar forum-bar">Forums<div class="sponsor">Sponsored by:<span>88x31</span></div></div>
  <h3 class="abs sub-title forum-title">Industry Discussions and Help</h3>
  <ul class="abs forum-list">
    <li><svg width="26" height="22" viewBox="0 0 26 22"><path d="M2 2h16v10H8l-5 4v-4H2Z" fill="#3b9fe0"/><path d="M10 8h14v10h-2v3l-4-3h-8Z" fill="#8cc63f"/></svg>Beaten!</li>
    <li><svg width="26" height="22" viewBox="0 0 26 22"><path d="M2 2h16v10H8l-5 4v-4H2Z" fill="#3b9fe0"/><path d="M10 8h14v10h-2v3l-4-3h-8Z" fill="#8cc63f"/></svg>Need SMTP server for mass emailing</li>
    <li><svg width="26" height="22" viewBox="0 0 26 22"><path d="M2 2h16v10H8l-5 4v-4H2Z" fill="#3b9fe0"/><path d="M10 8h14v10h-2v3l-4-3h-8Z" fill="#8cc63f"/></svg>Hosting Options</li>
    <li><svg width="26" height="22" viewBox="0 0 26 22"><path d="M2 2h16v10H8l-5 4v-4H2Z" fill="#3b9fe0"/><path d="M10 8h14v10h-2v3l-4-3h-8Z" fill="#8cc63f"/></svg>Funny Customer Service Inquiries</li>
    <li><svg width="26" height="22" viewBox="0 0 26 22"><path d="M2 2h16v10H8l-5 4v-4H2Z" fill="#3b9fe0"/><path d="M10 8h14v10h-2v3l-4-3h-8Z" fill="#8cc63f"/></svg>What to do you use to develop websites ?</li>
    <li><svg width="26" height="22" viewBox="0 0 26 22"><path d="M2 2h16v10H8l-5 4v-4H2Z" fill="#3b9fe0"/><path d="M10 8h14v10h-2v3l-4-3h-8Z" fill="#8cc63f"/></svg>Blogcraft Spam</li>
    <li><svg width="26" height="22" viewBox="0 0 26 22"><path d="M2 2h16v10H8l-5 4v-4H2Z" fill="#3b9fe0"/><path d="M10 8h14v10h-2v3l-4-3h-8Z" fill="#8cc63f"/></svg>PH Directory</li>
    <li><svg width="26" height="22" viewBox="0 0 26 22"><path d="M2 2h16v10H8l-5 4v-4H2Z" fill="#3b9fe0"/><path d="M10 8h14v10h-2v3l-4-3h-8Z" fill="#8cc63f"/></svg>36 More SEO Myths</li>
    <li><svg width="26" height="22" viewBox="0 0 26 22"><path d="M2 2h16v10H8l-5 4v-4H2Z" fill="#3b9fe0"/><path d="M10 8h14v10h-2v3l-4-3h-8Z" fill="#8cc63f"/></svg>'Rotating' Newsboard &amp; SEO</li>
    <li><svg width="26" height="22" viewBox="0 0 26 22"><path d="M2 2h16v10H8l-5 4v-4H2Z" fill="#3b9fe0"/><path d="M10 8h14v10h-2v3l-4-3h-8Z" fill="#8cc63f"/></svg>Searchly's new look</li>
  </ul>
  <a class="abs more forum-all">See all discussions</a>

  <!-- right column ads -->
  <div class="ad" style="left:783px;top:1430px;width:345px;height:142px">
    <span class="ad-tag">Add</span>
    <div class="ad-area" style="left:6px;top:22px;width:320px;height:110px">3:1 Rectangle<br>300x100</div>
  </div>
  <div class="ad" style="left:783px;top:1597px;width:345px;height:102px">
    <span class="ad-tag">Add</span>
    <div class="ad-area" style="left:44px;top:22px;width:240px;height:66px;padding-left:46px">Half Banner<br>234x60</div>
  </div>
  <div class="ad" style="left:783px;top:1720px;width:345px;height:100px">
    <span class="ad-tag">Add</span>
    <div class="ad-area" style="left:102px;top:22px;width:128px;height:70px;padding-left:10px">Button 2<br>120x60</div>
  </div>
  <div class="ad" style="left:783px;top:1843px;width:345px;height:131px">
    <span class="ad-tag">Add</span>
    <div class="ad-area" style="left:102px;top:20px;width:128px;height:104px;padding:26px 0 0 10px">Button 1<br>120x90</div>
  </div>

  <!-- footer -->
  <footer class="abs footer">
    <div class="abs foot-links">Home &nbsp;|&nbsp; Forums &nbsp;|&nbsp; Videos &nbsp;|&nbsp; Articles &nbsp;|&nbsp; Publications &nbsp;|&nbsp; SEO Blog &nbsp;|&nbsp; Marketing Blog &nbsp;|&nbsp; Resources &nbsp;|&nbsp; Advertise &nbsp;|&nbsp; RSS Feeds &nbsp;|&nbsp; Contact Us</div>
    <div class="abs foot-copy">Copyright 2004 - 2010 Pagelore-Hub.com &nbsp;| <b>Privacy Policy</b> | <b>Affiliate Disclaimer</b></div>
  </footer>

</div>
</body>
</html>
```